依頼詳細
PCとスマホデザインの両方納品をいただきますが、
まずはデザインイメージが確認しやすいPCページのみの提案をお願いします。
スマホページは当選者に納品時にお願いしたいと思います。
スマホサイズについて、カンバスサイズは横幅375pxで作成し、2倍の横幅750pxのサイズで書き出ししてください。
(Retinaディスプレイに対応するため)
スマホページ作成時は、メニューが展開した際のデザインもお願いします。
レスポンシブウェブデザインを意識したデザインでお願いします。

■サイトマップ
添付の画面遷移図をご確認ください。

■参考サイト
・サイトの雰囲気・イメージの参考サイト
https://mosvelu.jp/
・掲載製品の詳細
https://www.tovilka.co.jp/brand/palomix.html

■内容について
以下のサイトのリニューアルになります。
http://kuraden-shelf.jp/
倉庫ラックを製造していることと製品自体を紹介し、見積り依頼へアクションを促すサイトになります。
・公式サイト
https://www.hoben-tk.jp/

■素材写真
画像データについては、フリー素材から流用して
イメージ画像に当て込んでください。
足りない場合は、一旦他のサイトの写真をサンプルとして
入れてください。(サンプルなどの表記をお願いします)
また、購入が必要な写真などを利用した場合、
価格とサイト名を教えてください。

また、Adobe Stockで定期契約をしていますので、
Adobe Stockの画像は使用できます。
デザイン時はカンプ画像をお入れいただきますようお願いします。

■ワイヤーフレーム
https://wire.plenora.example/view/c39e27f0-5b1d-4a8e-9f62-b71d0e5a3c28-ab7d/?fullscreen
コンテンツの構成としてワイヤーフレームを作成しましたが
必ずしもワイヤーフレームの通りではなくて大丈夫です。
TOPページに配置するコンテンツを見ていただき、デザインは
デザイナーの皆様におまかせしたいと思います。

----------------------------------------------------------------------------
【制作物に対するお願い】

■フォントについて
・無料で使えるフォントで作成をお願いします。
・OSに紐づくフォントの使用は控えていただければと思います (ヒラギノなど)

■メインビジュアルについて
メインビジュアルは今のところスライドの予定です。
可能であれば以下の内容でメインビジュアルも作成していただきたいです。
①パロミクスについての紹介
②特価品のキャンペーン(今まで作成していた倉庫ラックを特価で販売する、といった内容)
③受注生産なので色やサイズなど色々カスタマイズ可能

シンプル 複雑
単色 カラフル
暗い 明るい
日常 高級
遊び心 厳粛
未来的 伝統的
女性的 男性的
ベースカラー:白、ポイントカラー:濃い目の緑(公式サイトのカラー)
• 高解像度JPG (.jpg)
• イラストレーター形式 (.ai)
• フォトショップ形式 (.psd)
上記のいずれか1つ(アウトラインありとなしの2つ)と高解像度JPGを納品お願いします。
adobe XDでの納品も可能です。

```html
<!DOCTYPE html>
<html lang="ja">
<head>
<meta charset="utf-8">
<title>沢野製作所 | パロミクス</title>
<link href="https://fonts.googleapis.com/css2?family=Noto+Sans+JP:wght@400;500;700&family=Montserrat:wght@500;600&display=swap" rel="stylesheet">
<style>
:root{
  --green:#24621f;
  --green-dark:#1a4b17;
  --green-mid:#3d8a2f;
  --green-light:#6db33f;
  --green-pale:#edf5e6;
  --ink:#2b2b2b;
  --muted:#6b6b6b;
  --line:#e2e2e2;
  --white:#ffffff;
  --gray-bg:#f4f4f2;
}
*{box-sizing:border-box;margin:0;padding:0}
html,body{width:1200px;height:5164px;overflow:hidden}
body{font-family:"Noto Sans JP",sans-serif;color:var(--ink);background:var(--white);position:relative;font-size:13px;line-height:1.8}
section,header,footer{position:absolute;left:0;width:1200px}
.abs{position:absolute}
.en{font-family:"Montserrat",sans-serif;color:var(--green-light);font-size:11px;letter-spacing:.08em}
.sec-title{text-align:center}
.sec-title h2{font-size:26px;font-weight:700;letter-spacing:.08em;line-height:1.4}
.photo{border-radius:0}
.btn-pill{display:flex;align-items:center;justify-content:space-between;background:var(--green);color:var(--white);border-radius:24px;padding:0 22px;font-size:13px;font-weight:500}

/* header */
.site-header{top:0;height:72px;background:var(--white)}
.brand{left:24px;top:22px;display:flex;align-items:center;gap:8px;font-size:20px;font-weight:700;color:var(--green)}
.brand .mark{width:24px;height:24px;background:var(--green)}
.gnav{left:420px;top:24px;display:flex;gap:34px;font-size:13px}
.hbtn{top:0;width:60px;height:72px;display:flex;flex-direction:column;align-items:center;justify-content:center;font-size:10px;gap:4px}
.hbtn.quote{left:1080px;background:var(--green-pale);color:var(--green)}
.hbtn.contact{left:1140px;background:var(--green);color:var(--white)}

/* hero */
.hero{top:72px;height:600px}
.slide-side{top:30px;height:500px;width:130px;background:linear-gradient(160deg,#b84a3c,#7a8387);opacity:.45}
.slide-main{left:150px;top:30px;width:900px;height:500px;background:linear-gradient(135deg,#9aa0a3 0%,#c9c9c6 40%,#c0413a 75%,#8e2b25 100%)}
.hero-copy{left:190px;top:70px}
.hero-copy .name{font-size:40px;font-weight:700;color:var(--white);letter-spacing:.06em;margin-bottom:18px}
.hero-copy .lead{display:inline-block;background:var(--green-dark);color:var(--white);font-size:18px;font-weight:700;padding:6px 16px}
.hero-copy .up{display:inline-block;margin-top:8px;background:#c3342a;color:var(--white);font-size:22px;font-weight:700;padding:6px 16px}
.arrow{top:250px;width:36px;height:36px}
.dots{top:550px;left:0;width:1200px;display:flex;justify-content:center;gap:10px}
.dots i{width:8px;height:8px;border-radius:50%;background:#cfcfcf}
.dots i.on{background:var(--green)}

/* about */
.about{top:700px;height:340px}
.about .photo{left:0;top:20px;width:600px;height:290px;background:linear-gradient(120deg,#a8442f,#c9a67a 50%,#8e8f8a)}
.about .txt{left:650px;top:30px;width:420px}
.about h2{font-size:24px;color:var(--green);font-weight:700;line-height:1.3}
.about p{margin-top:22px;color:var(--ink)}
.about .btn-pill{position:absolute;left:650px;top:245px;width:220px;height:46px}

/* products */
.products{top:1140px;height:780px;background:var(--green)}
.panel{left:100px;top:30px;width:1000px;height:720px;background:var(--white)}
.panel .sec-title{margin-top:40px}
.panel .desc{text-align:center;color:var(--muted);margin-top:22px;font-size:13px}
.pcards{position:absolute;left:50px;top:230px;display:flex;gap:40px}
.pcard{width:270px;height:430px;background:var(--white);box-shadow:0 2px 10px rgba(0,0,0,.12);position:relative}
.pcard .img{height:200px;background:linear-gradient(150deg,#f3f3f3,#d9d9d9)}
.pcard h3{font-size:16px;font-weight:700;margin:18px 18px 8px;color:var(--ink)}
.pcard p{margin:0 18px;font-size:12px;color:var(--muted)}
.pcard .go{position:absolute;left:0;bottom:0;width:100%;height:44px;background:var(--green);color:var(--white);display:flex;align-items:center;justify-content:flex-end;padding-right:20px;font-size:12px;gap:8px}

/* cases */
.cases{top:1960px;height:760px;background-color:#fafafa;background-image:radial-gradient(#dcdcdc 1px,transparent 1px);background-size:14px 14px}
.cases .sec-title{margin-top:40px}
.ccards{position:absolute;left:150px;top:140px;display:flex;gap:40px}
.ccard{width:273px;height:450px;background:var(--white);box-shadow:0 2px 10px rgba(0,0,0,.1);position:relative}
.ccard .img{height:190px}
.ccard h3{font-size:15px;font-weight:700;margin:16px 18px 10px;line-height:1.6}
.ccard p{margin:0 18px;font-size:12px;color:var(--muted)}
.ccard .tag{position:absolute;left:18px;bottom:26px;background:var(--green);color:var(--white);font-size:10px;padding:2px 10px;border-radius:10px}
.ccard .co{position:absolute;right:18px;bottom:24px;font-size:12px}
.more{left:510px;top:670px;width:180px;height:44px;justify-content:center;gap:10px}

/* contact */
.contact{top:2760px;height:390px;background:linear-gradient(90deg,var(--green-dark),var(--green) 60%,#3a7a32);color:var(--white)}
.contact .sec-title{margin-top:40px}
.contact .sec-title .en{color:#cfe6bf}
.contact .lead{text-align:center;margin-top:16px;font-size:13px}
.tel{left:150px;top:250px}
.tel small{display:block;font-size:11px}
.tel b{font-family:"Montserrat",sans-serif;font-size:32px;font-weight:600;display:flex;align-items:center;gap:8px;line-height:1.2}
.cbtn{top:258px;width:240px;height:56px;background:var(--white);color:var(--green);display:flex;align-items:center;justify-content:space-between;padding:0 22px;font-weight:700;font-size:14px}

/* company */
.company{top:3160px;height:400px}
.company .left{left:150px;top:40px;width:420px}
.company h2{font-size:24px;font-weight:700}
.company p{margin-top:18px;font-size:12px;color:var(--muted)}
.clinks{margin-top:26px;border-top:1px solid var(--line)}
.clinks li{list-style:none;display:flex;justify-content:space-between;border-bottom:1px solid var(--line);padding:14px 6px;font-size:13px}
.company .photo{left:630px;top:60px;width:420px;height:260px;background:linear-gradient(180deg,#bcd9ee 0%,#dfeaf2 40%,#3a3d42 45%,#2c2f33 85%,#9c9c98 100%)}

/* news */
.news{top:3600px;height:380px;background:var(--green-pale)}
.news .left{left:150px;top:70px}
.news h2{font-size:24px;font-weight:700}
.news .box{left:380px;top:40px;width:670px;height:300px;background:var(--white);padding:20px 30px}
.nrow{display:flex;align-items:center;gap:18px;padding:14px 0;border-bottom:1px solid var(--line);font-size:12px}
.nrow .tag{border:1px solid var(--green-light);color:var(--green-light);font-size:10px;padding:0 8px}
.nrow time{color:var(--muted);font-family:"Montserrat",sans-serif}

/* faq */
.faq{top:4020px;height:860px}
.faq .sec-title{margin-top:30px}
.faqlist{position:absolute;left:150px;top:130px;width:900px}
.q{display:flex;align-items:center;gap:14px;height:58px;border-bottom:1px solid var(--line);font-size:13px;padding:0 10px}
.q .ico,.a .ico{width:22px;height:22px;border-radius:50%;background:var(--green);color:var(--white);font-family:"Montserrat",sans-serif;font-size:11px;display:flex;align-items:center;justify-content:center;flex:none}
.q .tog{margin-left:auto;color:var(--green);font-size:18px}
.a{display:flex;gap:14px;padding:16px 10px;background:var(--green-pale);font-size:12px;color:var(--muted)}
.a .ico{background:var(--green-light)}

/* footer */
.site-footer{top:4880px;height:284px;background:var(--gray-bg)}
.site-footer .brand{left:150px;top:40px}
.faddr{left:150px;top:90px;font-size:11px;color:var(--muted);line-height:1.9}
.fcol{top:40px;font-size:12px;line-height:2.4}
.fcol li{list-style:none}
.fcol .sub{font-size:11px;color:var(--muted);padding-left:12px}
.copy{left:0;bottom:0;width:1200px;height:40px;background:var(--green);color:var(--white);font-size:10px;display:flex;align-items:center;justify-content:center}
.totop{left:1120px;top:176px;width:48px;height:48px;background:var(--green-light);display:flex;align-items:center;justify-content:center}
</style>
</head>
<body>

<header class="site-header">
  <div class="abs brand"><span class="mark"></span>沢野製作所</div>
  <nav class="abs gnav">
    <span>パロミクスについて</span><span>製品一覧 ▾</span><span>導入事例</span><span>会社概要</span><span>お知らせ</span><span>よくある質問</span>
  </nav>
  <div class="abs hbtn quote">
    <svg width="20" height="20" viewBox="0 0 20 20"><rect x="4" y="2" width="12" height="16" fill="none" stroke="currentColor" stroke-width="1.6"/><path d="M7 7h6M7 10h6M7 13h4" stroke="currentColor" stroke-width="1.4"/></svg>見積依頼
  </div>
  <div class="abs hbtn contact">
    <svg width="20" height="20" viewBox="0 0 20 20"><path d="M2 9l16-7-6 16-3-6z" fill="currentColor"/></svg>お問い合わせ
  </div>
</header>

<section class="hero">
  <div class="abs slide-side" style="left:0" role="img" aria-label="前のスライドの倉庫ラック写真"></div>
  <div class="abs slide-side" style="left:1070px" role="img" aria-label="次のスライドの倉庫ラック写真"></div>
  <div class="abs slide-main" role="img" aria-label="倉庫に積み重ねられた赤いパロミクスの写真"></div>
  <div class="abs hero-copy">
    <div class="name">パロミクス</div>
    <div class="lead">倉庫や工場の限られたスペースを有効活用し</div><br>
    <div class="up">収納効率大幅UP!</div>
  </div>
  <svg class="abs arrow" style="left:112px" viewBox="0 0 36 36"><path d="M22 8l-10 10 10 10" fill="none" stroke="#333" stroke-width="2.5"/></svg>
  <svg class="abs arrow" style="left:1052px" viewBox="0 0 36 36"><path d="M14 8l10 10-10 10" fill="none" stroke="#333" stroke-width="2.5"/></svg>
  <div class="abs dots"><i class="on"></i><i></i><i></i></div>
</section>

<section class="about">
  <div class="abs photo" role="img" aria-label="段ボールを積んだパロミクスが並ぶ倉庫の写真"></div>
  <div class="abs txt">
    <h2>パロミクスについて</h2>
    <div class="en">About</div>
    <p>パロミクスとは、限られたスペースを有効に活用し、保管効率と省電力化のために生まれた画期的なラックシステムです。</p>
  </div>
  <div class="btn-pill">詳しくはこちら<span>→</span></div>
</section>

<section class="products">
  <div class="abs panel">
    <div class="sec-title"><h2>製品一覧</h2><div class="en">Product</div></div>
    <p class="desc">2〜4段の積み重ねを実現することにより、限られた倉庫のスペースを有効活用。<br>パレットを平置きにした場合と、パロミクスを3段に積み重ねた場合、平置きスペースは少なくとも済みます。<br>各製品のサイズやカスタマイズ内容については各製品ページをご確認ください。</p>
    <div class="pcards">
      <div class="pcard"><div class="img" role="img" aria-label="赤いパロミクス本体の製品写真"></div><h3>パロミクス</h3><p>2段〜4段までの積み重ねに対応した基本型。大型パレットの保管に最適です。</p><div class="go">詳細へ <span>›</span></div></div>
      <div class="pcard"><div class="img" role="img" aria-label="段パロミクスの製品写真"></div><h3>段パロミクス</h3><p>荷物を置く段の高さを調整できるタイプ。多様な荷姿に柔軟に対応します。</p><div class="go">詳細へ <span>›</span></div></div>
      <div class="pcard"><div class="img" role="img" aria-label="網付きオプションパーツの製品写真"></div><h3>オプションパーツ</h3><p>パロミクスをより使いやすくする各種パーツをご用意しています。</p><div class="go">詳細へ <span>›</span></div></div>
    </div>
  </div>
</section>

<section class="cases">
  <div class="sec-title"><h2>導入事例</h2><div class="en">Case study</div></div>
  <div class="ccards">
    <div class="ccard"><div class="img" role="img" aria-label="倉庫に並ぶパロミクスの導入写真" style="background:linear-gradient(140deg,#b5453a,#d9d4ce)"></div><h3>パロミクスを導入して、置けることが実現されました。</h3><p>既存のスペースを有効に活用し、保管量を大きく増やすことができました。</p><span class="tag">製造業</span><span class="co">〇〇商事 様</span></div>
    <div class="ccard"><div class="img" role="img" aria-label="倉庫内で荷物を保管する様子の写真" style="background:linear-gradient(140deg,#c8b8a4,#8b8f92)"></div><h3>資材に利用させていただいています</h3><p>資材の保管効率が上がり、作業の流れもスムーズになりました。</p><span class="tag">物流倉庫</span><span class="co">〇〇運送 様</span></div>
    <div class="ccard"><div class="img" role="img" aria-label="導入企業の担当者の写真" style="background:linear-gradient(140deg,#d6d2cc,#9ea39c)"></div><h3>収納効率が「4倍」になり、倉庫を有効活用。</h3><p>限られた倉庫でも収納量が大幅に増え、とても満足しています。</p><span class="tag">卸売業</span><span class="co">〇〇産業 様</span></div>
  </div>
  <div class="abs btn-pill more">もっと見る <span>→</span></div>
</section>

<section class="contact" aria-label="お問い合わせ">
  <div class="sec-title"><h2>お問い合わせ</h2><div class="en">Contact</div></div>
  <p class="lead">パロミクスに関するご相談・ご質問・お見積りなどお気軽にお問い合わせください。<br>電話・メール（お問い合わせフォーム）よりご連絡いただけます。</p>
  <div class="abs tel"><small>お電話はこちらから</small><b><svg width="26" height="26" viewBox="0 0 24 24"><path d="M6.6 10.8a15 15 0 006.6 6.6l2.2-2.2a1 1 0 011-.25 11.4 11.4 0 003.6.6 1 1 0 011 1V20a1 1 0 01-1 1A17 17 0 013 4a1 1 0 011-1h3.5a1 1 0 011 1 11.4 11.4 0 00.6 3.6 1 1 0 01-.25 1z" fill="#fff"/></svg>0256-47-2918</b></div>
  <div class="abs cbtn" style="left:540px"><span>✉ お問い合わせ</span><span>›</span></div>
  <div class="abs cbtn" style="left:820px"><span>見積依頼はこちら</span><span>›</span></div>
</section>

<section class="company">
  <div class="abs left">
    <h2>会社概要</h2><div class="en">Company</div>
    <p>沢野製作所は創業以来、ものづくりの技術を活かし、倉庫ラックの製造を行っております。お客様の声を大切にし、高品質な製品をお届けいたします。</p>
    <ul class="clinks"><li>企業概要<span>›</span></li><li>会社沿革<span>›</span></li><li>代表メッセージ<span>›</span></li></ul>
  </div>
  <div class="abs photo" role="img" aria-label="沢野製作所の社屋外観の写真"></div>
</section>

<section class="news">
  <div class="abs left"><h2>お知らせ</h2><div class="en">News</div></div>
  <div class="abs box">
    <div class="nrow"><span class="tag">お知らせ</span><time>2022.10.00</time><span>テキストが入ります。テキストが入ります。テキストが入ります。</span></div>
    <div class="nrow"><span class="tag">お知らせ</span><time>2022.10.00</time><span>テキストが入ります。テキストが入ります。テキストが入ります。</span></div>
    <div class="nrow"><span class="tag">お知らせ</span><time>2022.10.00</time><span>テキストが入ります。テキストが入ります。テキストが入ります。</span></div>
    <div class="nrow"><span class="tag">お知らせ</span><time>2022.10.00</time><span>テキストが入ります。テキストが入ります。テキストが入ります。</span></div>
  </div>
</section>

<section class="faq">
  <div class="sec-title"><h2>よくある質問</h2><div class="en">FAQ</div></div>
  <div class="faqlist">
    <div class="q"><span class="ico">Q</span>どのくらいのサイズまで製造可能ですか？<span class="tog">−</span></div>
    <div class="a"><span class="ico">A</span>ご希望のサイズに合わせて製作いたします。詳しくはお気軽にお問い合わせください。</div>
    <div class="q"><span class="ico">Q</span>色のカスタマイズは可能ですか？<span class="tog">+</span></div>
    <div class="q"><span class="ico">Q</span>パロミクスの耐荷重はどのくらいですか？<span class="tog">+</span></div>
    <div class="q"><span class="ico">Q</span>見積りの依頼方法を教えてください。<span class="tog">+</span></div>
    <div class="q"><span class="ico">Q</span>既存の倉庫のパレットを使うことはできますか？<span class="tog">+</span></div>
    <div class="q"><span class="ico">Q</span>少数の注文にも対応していただけますか？<span class="tog">+</span></div>
    <div class="q"><span class="ico">Q</span>納品までの期間を教えてください。<span class="tog">+</span></div>
    <div class="q"><span class="ico">Q</span>組み立ては必要ですか？<span class="tog">+</span></div>
    <div class="q"><span class="ico">Q</span>製品の保証や修理について対応していますか？<span class="tog">+</span></div>
  </div>
</section>

<footer class="site-footer">
  <div class="abs brand"><span class="mark"></span>沢野製作所</div>
  <div class="abs faddr">〒955-0000<br>新潟県三条市東町1-2-3<br>TEL：0256-47-2918<br>FAX：0256-47-2919</div>
  <ul class="abs fcol" style="left:420px"><li>› パロミクスについて</li><li>› 製品一覧</li><li class="sub">- パロミクス</li><li class="sub">- 段パロミクス</li><li class="sub">- オプションパーツ</li></ul>
  <ul class="abs fcol" style="left:600px"><li>› 導入事例</li><li>› よくある質問</li><li>› 会社概要</li><li>› お知らせ</li></ul>
  <ul class="abs fcol" style="left:780px"><li>› お問い合わせ</li><li>› 見積依頼</li><li>› プライバシーポリシー</li><li>› サイトマップ</li></ul>
  <div class="abs totop"><svg width="18" height="18" viewBox="0 0 18 18"><path d="M3 12l6-6 6 6" fill="none" stroke="#fff" stroke-width="2.2"/></svg></div>
  <div class="abs copy">Copyright © SAWANO SEISAKUSHO All rights reserved.</div>
</footer>

</body>
</html>
```